Family Farm Looking for meat label

We have a small farm in Italy with two types of cow "Piemontese" and "Pezzata Rossa Valdostana". We need label ( about 5x5 cm) to put on the boxes and on every single piece of meat.

Target Market(s)

private client

Industry/Entity Type

family farm

Colors

Designer to choose colors to be used in the design.

Requirements
Must have
• to write "Azienda Agricola Il Roveto" and the cow like our cow not differently. the Piemontese breed cow has the typical physical shapes as in the photo. No photo on the label just a drawing o something like that.
Nice to have
• just a one label, clear, fine and clean . Maybe with pastel color or watercolor. We are a small family farm.
Should not have
• no photo, no another type of cow

```html
<!DOCTYPE html>
<html lang="en">
<head>
<meta charset="utf-8">
<title>Il Roveto – Piemontese Beef Label</title>
<link href="https://fonts.googleapis.com/css2?family=Montserrat:wght@800&family=Bebas+Neue&family=Barlow:wght@300&display=swap" rel="stylesheet">
<style>
  :root {
    --stage: #3a3a3c;
    --paper: #efede6;
    --farm-red: #b5161d;
    --meadow: #2ba44a;
    --label-ink: #f2f2f2;
    --sketch-tone: rgba(40, 40, 40, 0.07);
  }
  * { margin: 0; padding: 0; box-sizing: border-box; }
  html, body {
    width: 1200px;
    height: 791px;
    overflow: hidden;
    background: var(--stage);
  }
  .label {
    position: absolute;
    left: 240px;
    top: 35px;
    width: 720px;
    height: 720px;
    background: var(--paper);
    overflow: hidden;
  }
  .farm-band {
    position: absolute;
    left: 0; top: 0;
    width: 100%;
    height: 51px;
    background: var(--farm-red);
    display: flex;
    align-items: center;
    justify-content: center;
    color: var(--label-ink);
    font-family: "Montserrat", sans-serif;
    font-weight: 800;
    font-size: 35px;
    letter-spacing: 0.5px;
    text-transform: uppercase;
    white-space: nowrap;
  }
  .roof {
    position: absolute;
    left: 0; top: 0;
    width: 720px;
    height: 720px;
  }
  .cow-sketch {
    position: absolute;
    left: 0;
    top: 190px;
    width: 490px;
    height: 400px;
    background: linear-gradient(120deg, var(--sketch-tone), rgba(40,40,40,0.03));
    border-radius: 40px 180px 60px 20px;
  }
  .farm-name {
    position: absolute;
    left: 310px;
    top: 170px;
    font-family: "Montserrat", sans-serif;
    font-weight: 800;
    font-size: 40px;
    line-height: 1;
    color: var(--farm-red);
    white-space: nowrap;
  }
  .product-name {
    position: absolute;
    left: 35px;
    top: 442px;
    font-family: "Bebas Neue", sans-serif;
    font-size: 126px;
    line-height: 0.82;
    color: var(--label-ink);
  }
  .claims {
    position: absolute;
    left: 30px;
    top: 662px;
    font-family: "Barlow", sans-serif;
    font-weight: 300;
    font-size: 31px;
    color: var(--label-ink);
    word-spacing: 4px;
    white-space: nowrap;
  }
</style>
</head>
<body>
  <main class="label">
    <svg class="roof" viewBox="0 0 720 720" aria-hidden="true">
      <polygon points="0,446 274,310 720,568 720,720 0,720" fill="var(--meadow)"/>
      <polyline points="0,420 274,292 720,546" fill="none" stroke="var(--meadow)" stroke-width="5"/>
    </svg>
    <div class="cow-sketch" role="img" aria-label="Line drawing of a Piemontese calf with its head lowered"></div>
    <header class="farm-band">Azienda Agricola Il Roveto</header>
    <div class="farm-name">Il Roveto</div>
    <h1 class="product-name">Piemontese<br>Beef</h1>
    <p class="claims">100% Natural&nbsp; NO antibiotics&nbsp; No hormones</p>
  </main>
</body>
</html>
```